HTML formatted email for Havenstrix

Create a single email in html format to describe the Havenstrix product.

It needs to be based on the brochure design (supplied) and using existing logo.
One requirement is that the background of the email has to be a set color (grey), regardless of how large the viewer opens the email window.
It will be a mix of graphics and text: and the central block of content within the email must remain intact and true regardless of how the viewer resizes the email window.
The html email must be viewable in it true format on all common email programs, including Microsoft Outlook, horde, gmail and others.

The attached file is for reference only, full PSD will be supplied to winner. (The actual text content will be different to the sample file)

```html
<!DOCTYPE html>
<html lang="en">
<head>
<meta charset="utf-8">
<title>Havenstrix – Email</title>
<link href="https://fonts.googleapis.com/css2?family=Arimo:wght@400;700&family=Noto+Serif:ital,wght@0,400;0,700;1,400&display=swap" rel="stylesheet">
<style>
:root{
  --page:#3b3b3b;
  --page-dark:#2f2f2f;
  --white:#ffffff;
  --panel:#e8e8e8;
  --panel-line:#cfcfcf;
  --dark-panel:#262626;
  --ink:#2a2a2a;
  --muted:#8a8a8a;
  --muted-dark:#b8b8b8;
  --brand:#3c9fd0;
  --accent:#4aa9c9;
  --accent-dark:#2f8aa8;
}
*{margin:0;padding:0;box-sizing:border-box}
html,body{width:1200px;height:2340px;overflow:hidden}
body{background:var(--page);font-family:"Noto Serif",Georgia,serif;color:var(--ink);position:relative}
.email{position:absolute;left:48px;top:0;width:1112px}

.header{position:relative;height:248px;background:var(--white)}
.brand{position:absolute;left:28px;top:40px;display:flex;align-items:center;gap:16px}
.brand-mark{width:64px;height:64px;border-radius:50%;background:var(--brand)}
.brand-name{font-family:"Arimo",Arial,sans-serif;font-size:58px;color:var(--brand);font-weight:400}
.nav{position:absolute;right:16px;top:46px;display:flex;gap:28px;font-style:italic;font-size:26px;color:var(--ink)}
.nav-rule{position:absolute;left:470px;right:16px;top:100px;height:2px;background:var(--panel-line)}
.tagline{position:absolute;right:16px;top:118px;font-style:italic;font-size:25px}

.hero{height:432px;background:radial-gradient(ellipse at 55% 40%,#3f7fb0 0%,#1d3f63 45%,#0c1a2c 100%)}

.step-head{display:flex;align-items:center;gap:22px}
.step-num{width:72px;height:72px;border-radius:50%;display:flex;align-items:center;justify-content:center;font-family:"Arimo",Arial,sans-serif;font-weight:700;font-size:40px}
.step-title{font-family:"Arimo",Arial,sans-serif;font-weight:700;font-size:34px}

.intro{height:340px;background:var(--panel);padding:28px 20px 0}
.intro .step-num{background:var(--ink);color:var(--white)}
.intro .step-title{color:var(--ink)}
.intro p{margin-top:24px;font-size:23px;line-height:1.45;color:var(--muted)}

.advantage{position:absolute;top:1048px;left:0;width:1112px;height:352px;background:var(--dark-panel);padding:28px 20px 0;border:2px solid #3f3f3f}
.advantage .step-num{background:var(--white);color:var(--ink)}
.advantage .step-title{color:var(--accent)}
.advantage p{margin-top:24px;font-size:23px;line-height:1.5;color:var(--muted-dark)}
.advantage p.aside{margin-top:4px;font-style:italic}
.btn{position:absolute;right:14px;bottom:22px;background:linear-gradient(var(--accent),var(--accent-dark));color:var(--white);font-family:"Arimo",Arial,sans-serif;font-weight:700;font-size:26px;padding:18px 26px;border-radius:4px}
.accent-rule{position:absolute;top:1404px;left:0;width:1112px;height:12px;background:var(--accent)}

.columns{position:absolute;top:1440px;left:0;width:1112px;height:580px;background:var(--panel);display:flex;gap:60px;padding:20px 28px 0}
.col{flex:1}
.col-visual{height:256px;border-radius:6px}
.col-visual.light{background:linear-gradient(#f4f4f4,#dcdcdc)}
.col-visual.dark{background:radial-gradient(ellipse at center,#4a4a4a,#1f1f1f)}
.columns .step-head{margin-top:26px}
.columns .step-num{background:var(--ink);color:var(--white);border-radius:6px;width:64px;height:64px;font-size:36px}
.columns .step-title{font-size:30px;color:var(--ink)}
.col-rule{height:2px;background:var(--panel-line);margin:18px 0 22px}
.columns p{font-size:22px;line-height:1.55;color:var(--muted)}

.footer{position:absolute;top:2060px;left:0;width:1112px;height:260px;color:#bdbdbd;font-size:18px;line-height:1.45}
.footer .notice{position:absolute;left:0;top:20px}
.footer .notice u{color:#dcdcdc}
.footer .contact{position:absolute;left:0;top:160px;color:#cfcfcf}
.social{position:absolute;right:0;top:78px;display:flex;gap:22px}
.social span{width:60px;height:60px;border-radius:50%;border:3px solid #9a9a9a;background:#4a4a4a}
.footer .phone{position:absolute;right:0;top:172px;font-size:20px;color:#8f8f8f;letter-spacing:2px}
</style>
</head>
<body>
<div class="email">
  <header class="header">
    <div class="brand"><span class="brand-mark"></span><span class="brand-name">Havenstrix</span></div>
    <nav class="nav"><span>Havenstrix</span><span>Services</span><span>Pricing</span><span>Benefits</span><span>Contact</span></nav>
    <div class="nav-rule"></div>
    <div class="tagline">Your Data - When you need it, where you need it</div>
  </header>

  <div class="hero" role="img" aria-label="Hand touching a glowing cloud network diagram on a dark blue background"></div>

  <section class="intro">
    <div class="step-head"><span class="step-num">1</span><h2 class="step-title">Havenstrix</h2></div>
    <p>Havenstrix is a service offered by Brantwell Group to businesses of all sizes. It's our answer to the Cloud services phenomenon.<br>
    It's everything you would expect from a cloud storage provider with one major advantage - your data is stored locally. That means you can access your information with or without internet access. It's secure, it's cost effective and it's easy.</p>
  </section>

  <section class="advantage">
    <div class="step-head"><span class="step-num">2</span><h2 class="step-title">The Havenstrix Advantage</h2></div>
    <p>Do you know where your data is right now? Who has access when your files are stored on the other side of the world? And what happens if you lose your internet connection?</p>
    <p class="aside">With Havenstrix, those worries are a thing of the past...</p>
    <span class="btn">Read More</span>
  </section>
  <div class="accent-rule"></div>

  <section class="columns">
    <div class="col">
      <div class="col-visual light" role="img" aria-label="Light grey illustration of small flat icons"></div>
      <div class="step-head"><span class="step-num">3</span><h3 class="step-title">Two column - text below</h3></div>
      <div class="col-rule"></div>
      <p>Velit esse cillum dolore eu fugiat nulla pariatur. Excepteur sint occaecat cupidatat non proident.</p>
    </div>
    <div class="col">
      <div class="col-visual dark" role="img" aria-label="Dark chalkboard with hand-lettered greeting"></div>
      <div class="step-head"><span class="step-num">4</span><h3 class="step-title">Two column - text below</h3></div>
      <div class="col-rule"></div>
      <p>Iste natus error sit voluptatem accusantium doloremque laudantium, totam rem aperiam, eaque ipsa quae ab illo inventore veritatis.</p>
    </div>
  </section>

  <footer class="footer">
    <p class="notice">You are receiving this email because:<br>1.) You're an awesome customer of "havenstrix" or<br>2.) You subscribed via <u>our website</u></p>
    <p class="contact">info@havenstrix.com</p>
    <div class="social"><span></span><span></span><span></span><span></span></div>
    <p class="phone">555 010 4477</p>
  </footer>
</div>
</body>
</html>
```